letterhead design

can you create a letterhead using the logo you created and the following:

318 W Dunhaven Elgin IL 60123
(p) 847-555-0143
(f) 847-555-0178
www.thebrantleylawgroup.com

Industry/Entity Type

Law

Requirements
Must have
• Use logo attached: must have address 318 W Dunhaven Elgin IL 60123 phone 847-555-0143 fax 847-555-0178
Should not have
• Nothing other thank logo and address/phone/website

```html
<!DOCTYPE html>
<html lang="en">
<head>
<meta charset="utf-8">
<title>Brantley Law Group Letterhead</title>
<link href="https://fonts.googleapis.com/css2?family=Marcellus&display=swap" rel="stylesheet">
<style>
  :root {
    --gold: #e2b05a;
    --ink: #141414;
    --backdrop: #ccd2d2;
    --paper: #ffffff;
    --watermark: #fbf6ee;
    --black: #000000;
  }
  * { margin: 0; padding: 0; box-sizing: border-box; }
  html, body {
    width: 1200px;
    height: 1028px;
    overflow: hidden;
    background: var(--backdrop);
    font-family: "Marcellus", serif;
  }
  .letterhead {
    position: absolute;
    left: 244px;
    top: 12px;
    width: 711px;
    height: 1004px;
    background: var(--paper);
    overflow: hidden;
  }
  .brand {
    position: absolute;
    left: 35px;
    top: 40px;
    display: flex;
    align-items: center;
    gap: 12px;
  }
  .brand-mark {
    width: 70px;
    height: 70px;
    border: 1.6px solid var(--gold);
    border-radius: 50%;
  }
  .brand-name {
    color: var(--gold);
    text-align: center;
    line-height: 1;
  }
  .brand-name .primary {
    display: block;
    font-size: 25px;
    letter-spacing: 0.5px;
  }
  .brand-name .secondary {
    display: flex;
    align-items: center;
    gap: 8px;
    margin-top: 4px;
    font-size: 12.5px;
    letter-spacing: 1.2px;
  }
  .brand-name .secondary::before,
  .brand-name .secondary::after {
    content: "";
    flex: 1;
    height: 1px;
    background: var(--gold);
  }
  .contact {
    position: absolute;
    right: 38px;
    top: 38px;
    list-style: none;
    color: var(--ink);
    font-size: 14.5px;
    text-align: right;
  }
  .contact li {
    display: flex;
    justify-content: flex-end;
    align-items: center;
    gap: 10px;
    height: 20.5px;
  }
  .contact li.address { margin-bottom: 14px; }
  .contact svg { width: 14px; height: 14px; flex: none; }
  .watermark {
    position: absolute;
    left: 221px;
    top: 333px;
    width: 360px;
    height: 360px;
    border: 8px solid var(--watermark);
    border-radius: 50%;
  }
  .footer-band {
    position: absolute;
    left: 0;
    bottom: 0;
    width: 711px;
    height: 15px;
  }
</style>
</head>
<body>
  <main class="letterhead">
    <header>
      <div class="brand">
        <div class="brand-mark"></div>
        <div class="brand-name">
          <span class="primary">BRANTLEY LAW</span>
          <span class="secondary">GROUP</span>
        </div>
      </div>

      <ul class="contact">
        <li class="address">318 W Dunhaven Elgin IL 60123
          <svg viewBox="0 0 16 16" aria-hidden="true"><path d="M8 1a4.5 4.5 0 0 0-4.5 4.5C3.5 9 8 13 8 13s4.5-4 4.5-7.5A4.5 4.5 0 0 0 8 1z" fill="none" stroke="#e2b05a" stroke-width="1.4"/><circle cx="8" cy="5.5" r="1.7" fill="#e2b05a"/><ellipse cx="8" cy="14" rx="4" ry="1.2" fill="none" stroke="#e2b05a" stroke-width="1"/></svg>
        </li>
        <li>847-555-0143
          <svg viewBox="0 0 16 16" aria-hidden="true"><path d="M4 2l2 3-1.3 1.3a8 8 0 0 0 5 5L11 10l3 2-1 2.5C7.5 14 2 8.5 1.5 3z" fill="#e2b05a"/></svg>
        </li>
        <li>847-555-0178
          <svg viewBox="0 0 16 16" aria-hidden="true"><rect x="2" y="6" width="12" height="8" rx="1" fill="#e2b05a"/><rect x="5" y="2" width="7" height="5" fill="none" stroke="#e2b05a" stroke-width="1.2"/><rect x="8" y="8" width="4" height="4" fill="#fff"/></svg>
        </li>
        <li>www.thebrantleylawgroup.com
          <svg viewBox="0 0 16 16" aria-hidden="true"><circle cx="8" cy="8" r="6.5" fill="#e2b05a"/><path d="M5 4c2 1 1 3 3 3s1 3-1 4M11 3c-1 2 1 3 2 4" fill="none" stroke="#fff" stroke-width="1.1"/></svg>
        </li>
      </ul>
    </header>

    <div class="watermark" aria-hidden="true"></div>

    <svg class="footer-band" viewBox="0 0 711 15" aria-hidden="true">
      <path d="M0 0H324q6 0 10 1.5L362 15H0z" fill="#e2b05a"/>
      <path d="M348 0H711V15H387q-4 0-8-1.5z" fill="#000"/>
    </svg>
  </main>
</body>
</html>
```